BRVL Brochure Design

Northfield Council of Clinical Standards (BRVL) needs a whole new brochure. I've upload EPS logos and past brochures. Our tagline is to "modernize healthcare" and we think our brochure should reflect that, so that's the purpose of this project.

BRVL is a proven leader in healthcare education, training and
consulting services for health professionals. We’ve earned a reputation for excellence in healthcare quality improvement and management.

BRVL works to improve healthcare quality by educating healthcare professionals about healthcare best practices. We focus on instructing our clients on how to plan for, measure, and improve healthcare quality in all facilities and facets such as:

Patient Safety
Infection Control
Performance Improvement
Risk Management
Compliance and Accreditation
Health and Hospital Administration
Health Insurance
Healthcare Financial Management
Facility Management and Safety

DESIGN SUGGESTIONS:

Brochure Size: 8.5 X 11 full size brochure or 8.5 X 11 trifold brochure

Number of Pages: 2 to 3

Colors: Feel free to use a wide array of colors but try to stay away from colors that are too loud, ex: Pink, Purple, Neon Green.

Themes: Professional, Educational

Designs:

Pelor by Oskar Lindqvist

Quorvo Pamphlet by Derek Malloway

Lanterns for harvest by Solvendri

Paisaje de Sr KT by vrpl

http://www.plimbask.com/post/28461937205/10-creative-brochure-designs

Don't limit yourself to these examples. However, these are examples we liked

Reason: We would like to see more designs

We want more full page designs than tri-fold 

We are considering both tri-fold and full-page but would like to see more full page designs 

Reason: Our lead designer making the decisions on this project has been fired. I apologize for the inconvenience. We want extend the project one last time

Target Market(s)

Students, Doctors, and Educational Professionals

Industry/Entity Type

Healthcare

Logo Text

asdfasdf

Font styles to use
Serif
Sans Serif
Decorative
Script

Requirements
Should not have
• Pink, Purple, Neon Green colors

```html
<!DOCTYPE html>
<html lang="en">
<head>
<meta charset="utf-8">
<title>BRVL Brochure – Inside Spread</title>
<link rel="stylesheet" href="https://fonts.googleapis.com/css2?family=Roboto+Condensed:wght@700&family=Roboto:wght@400;700&display=swap">
<style>
  :root{
    --navy:#1b2f92;
    --ink:#3447a3;
    --cyan:#22b7e6;
    --sky:#8fd3f0;
    --paper:#ffffff;
    --photo-light:#eef2f5;
    --photo-mid:#c9d3dc;
  }
  *{margin:0;padding:0;box-sizing:border-box}
  html,body{width:1200px;height:854px;overflow:hidden;background:var(--paper)}
  .spread{position:relative;width:1200px;height:854px;background:var(--paper);font-family:"Roboto",Arial,sans-serif;color:var(--ink);font-size:13.4px;line-height:21.6px}
  .panel{position:absolute;top:0;height:854px}
  .panel-about{left:0;width:405px}
  .panel-offer{left:432px;width:370px}
  .panel-prices{left:825px;width:350px}
  .heading{font-family:"Roboto Condensed",Arial,sans-serif;font-weight:700;color:var(--navy);font-size:31px;line-height:36px;letter-spacing:.3px}
  .panel-offer .heading,.panel-prices .heading{margin-top:48px;margin-bottom:16px}
  .hero-photo{position:absolute;left:0;top:0}
  .about-body{position:absolute;left:30px;top:385px;width:350px}
  .about-body .heading{margin-bottom:20px}
  .brand{font-weight:700;color:var(--navy)}
  .highlight{color:var(--cyan);font-weight:700;margin-top:22px}
  .sub{font-weight:700;color:var(--navy);margin-top:20px}
  .classes{list-style:none;color:var(--cyan);font-weight:700}
  .classes li::before{content:"• "}
  .bullets{list-style:none}
  .bullets li::before{content:"• "}
  .indent{padding-left:12px;text-indent:-12px}
  .portrait{position:absolute;left:950px;top:618px}
  .dues-strong{font-weight:700;color:var(--navy)}
  .narrow{width:200px}
</style>
</head>
<body>
<main class="spread">

  <section class="panel panel-about">
    <svg class="hero-photo" width="405" height="360" viewBox="0 0 405 360">
      <defs>
        <linearGradient id="heroFill" x1="0" y1="0" x2="1" y2="1">
          <stop offset="0" stop-color="var(--photo-mid)"/>
          <stop offset=".5" stop-color="var(--photo-light)"/>
          <stop offset="1" stop-color="#dfe6ec"/>
        </linearGradient>
      </defs>
      <path d="M0 0 H395 C400 150 340 300 0 320 Z" fill="url(#heroFill)" role="img" aria-label="Photo of a doctor in a white coat holding a tablet"/>
      <path d="M0 320 C340 300 400 150 395 0" fill="none" stroke="var(--navy)" stroke-width="9"/>
      <path d="M0 337 C360 318 412 160 404 0" fill="none" stroke="var(--sky)" stroke-width="5"/>
    </svg>

    <div class="about-body">
      <h2 class="heading">ABOUT US...</h2>
      <p><span class="brand">BRVL</span> is a proven leader in healthcare education, training and consulting services for health professionals. We’ve earned a reputation for excellence in healthcare quality improvement and management.</p>
      <p class="highlight">• Our senior technical staff works with some of the world’s top healthcare organizations.</p>
      <p class="highlight">• We’ve developed assessment systems healthcare leaders use to gauge their performance and accreditation standards used by the Global Care Standards Board (GCSB) and selected countries.</p>
      <p class="highlight">• Our training workshops on healthcare management, quality, insurance and a variety of other important topics have helped dozens of organizations across the globe.</p>
    </div>
  </section>

  <section class="panel panel-offer">
    <h2 class="heading">WHAT WE OFFER...</h2>
    <p>If you’re a healthcare professional or organization seeking top-notch professional development services, you’ve found what you’re looking for. Consider BRVL’s offerings:</p>
    <ul class="bullets">
      <li>Our workshops and seminars address teambuilding, leadership, quality assurance and improvement, accreditation, performance measurement, patient safety, risk management, utilization management, hospital surveying, customer service, standards and communication, strategic planning, applied research, survey design and methods, re-engineering, and the Six Sigma management method.</li>
      <li>Our national and international conferences on quality management attract audiences of more than 1,000 of the world’s leading health professionals.</li>
      <li>Our seminars cover cost benefit and effectiveness analysis, managed care, and medical informatics.</li>
      <li>Our consultants are always available to assess your needs and develop custom solutions for your facility.</li>
    </ul>
    <p class="sub">Our Classes</p>
    <ul class="classes">
      <li>Certificate In Healthcare Quality (Chq)</li>
      <li>Certified Professional In Infection Control (Cpic)</li>
      <li>Certificate In Healthcare Risk Management (Chrm)</li>
      <li class="indent">Certificate In Healthcare Performance Improvement (Chpi)</li>
      <li>Certificate In Hospital Surveying (Chs)</li>
      <li class="indent">Certificate In Health And Hospital Administration (Cphha)</li>
      <li>Certified Patient Safety Officer (Cpso)</li>
      <li>Fellowship Preparation Course (Fbrvl)</li>
    </ul>
  </section>

  <section class="panel panel-prices">
    <h2 class="heading">MEMBERSHIP PRICES...</h2>
    <p><span class="brand">BRVL offers</span> several kinds of membership to met your varied needs.</p>

    <p class="sub">Personal Membership</p>
    <p>If you want to become an BRVL member for your own personal and professional development, consider a personal membership. -<br>Annual Dues: $100 Apply Now</p>

    <p class="sub">Group Membership</p>
    <p>If you would like to procure membership for multiple people in your institution, consider a group membership, which offers:</p>
    <ul class="bullets">
      <li>membership for up to 15 people</li>
      <li class="indent">up to 3 subscriptions to the JBRVL, Journal of the Northfield Council of Clinical Standards</li>
    </ul>
    <p>Annual Dues: $350 Apply Now</p>

    <p class="sub">Student Membership</p>
    <p>If you are a student studying a health related field or have an interest in improving the quality of care available to the public, consider a student membership, which gives:</p>
    <ul class="bullets narrow">
      <li class="indent">all the benefits of regular membership</li>
      <li class="indent">special student rates to the BRVL conference</li>
    </ul>
    <p class="dues-strong" style="margin-top:18px">Annual Dues:<br>$25 Apply Now</p>
  </section>

  <svg class="portrait" width="250" height="236" viewBox="0 0 250 236">
    <defs>
      <linearGradient id="portraitFill" x1="0" y1="0" x2="1" y2="1">
        <stop offset="0" stop-color="#e4edf4"/>
        <stop offset="1" stop-color="#9fb4c9"/>
      </linearGradient>
    </defs>
    <path d="M250 22 C110 22 30 110 30 236 H250 Z" fill="url(#portraitFill)" role="img" aria-label="Photo of a smiling businessman in shirt and tie"/>
    <path d="M250 22 C110 22 30 110 30 236" fill="none" stroke="var(--navy)" stroke-width="9"/>
    <path d="M250 6 C96 6 12 100 14 236" fill="none" stroke="var(--sky)" stroke-width="5"/>
  </svg>

</main>
</body>
</html>
```